Single Side Postcard Size Flyer Design

We want to design an attractive and eye-catching sign for hair stylists and barbers to sit on their workstations to attract the attention of their clients regarding hair loss and encourage them to speak to their stylist about it of they are would like to seek treatment.
Many men and women suffer from hair loss, but are often in denial it is happening or too embarrassed to talk about it.
This postcard sized flyer is designed to stick to the mirror at their hair stylist or barber and encourage them to ask their stylist about it.
We want this to be very plain and simple. With just perhaps some kind of simple head line and worry lines. I have uploaded a simple idea.
I have also uploaded the print templates that must be used to provide final designs.

Target Market(s)

Men aged 25 to 60 with thinning hair

Industry/Entity Type

Healthcare

Font styles to use
Sans Serif

Colors
0355a3
ffffff
cfcfcf
1b1b1b

Requirements
Must have
• Flyer size is vertical 4" x 6"
• Copy for the flyer is as follows ans is in color blue: #014ca5
• Worried About Thinning Hair?
• 2 out of 3 Men will have visible hair loss by age 35.
• The Good News is that your
• Barber or Stylist can tell you how to
• stop the loss & grow back your hair.
• Just ask.
• The Brisk Lattice Program from
• The Marlow Pine Company
• New Science. No Surgery. Your Hair.
• www.quellvantinfo.example
Should not have
• - dont add any logos, images or ornate design. this needs to be simple, easy to ready and eye catching.
• - do not use the color red in any capacity.

```html
<!DOCTYPE html>
<html lang="en">
<head>
<meta charset="utf-8">
<title>Worried About Thinning Hair? – The Marlow Pine Company</title>
<link rel="stylesheet" href="https://fonts.googleapis.com/css2?family=Open+Sans:wght@400;700&family=Roboto+Slab:wght@500;600&display=swap">
<style>
  :root {
    --blue: #0b56a3;
    --ink: #1b1b1b;
    --paper: #e8e9ea;
    --grey-text: #555759;
    --frame: #6b6d70;
    --backdrop: #8a8a8a;
    --white: #ffffff;
  }
  * { margin: 0; padding: 0; box-sizing: border-box; }
  html, body { width: 960px; height: 1200px; overflow: hidden; background: var(--backdrop); }
  .flyer {
    position: absolute; left: 80px; top: 0;
    width: 800px; height: 1200px;
    background: var(--paper);
    overflow: hidden;
  }
  .line {
    position: absolute; left: 0; right: 0;
    text-align: center; white-space: nowrap;
    transform: translateY(-50%);
  }
  .slab { font-family: "Roboto Slab", Georgia, serif; }
  .sans { font-family: "Open Sans", Arial, sans-serif; }

  .headline { color: var(--blue); font-weight: 600; font-size: 74px; line-height: 1; letter-spacing: 1px; }
  .headline--one { top: 119px; }
  .headline--two { top: 196px; }

  .stat { top: 267px; font-size: 26px; color: var(--grey-text); }
  .stat__age { background: var(--blue); color: var(--white); font-weight: 700; padding: 0 3px; }

  .news-box {
    position: absolute; left: 58px; top: 375px;
    width: 686px; height: 191px;
    border: 2px solid var(--frame);
    border-radius: 42px 8px 42px 8px;
    border-top-right-radius: 18px; border-bottom-left-radius: 0;
    background: var(--paper);
  }
  .news-shadow {
    position: absolute; left: 60px; top: 566px;
    width: 680px; height: 40px;
    background: radial-gradient(ellipse at 50% 0%, rgba(0,0,0,0.55) 0%, rgba(0,0,0,0.15) 40%, rgba(0,0,0,0) 70%);
  }
  .news-lead { top: 433px; color: var(--blue); font-weight: 600; font-size: 33px; }
  .news-body { color: var(--grey-text); font-size: 29px; text-transform: uppercase; }
  .news-body--one { top: 478px; }
  .news-body--two { top: 510px; }

  .cta { top: 687px; color: var(--blue); font-weight: 600; font-size: 70px; }
  .program { top: 750px; color: var(--grey-text); font-weight: 500; font-size: 29px; }
  .web { top: 800px; color: var(--grey-text); font-weight: 600; font-size: 40px; }

  .wave { position: absolute; left: 0; top: 0; width: 800px; height: 1200px; }

  .company { top: 1067px; color: var(--white); font-weight: 500; font-size: 46px; }
  .tagline { top: 1120px; color: var(--white); font-size: 38px; }
</style>
</head>
<body>
  <main class="flyer">
    <svg class="wave" viewBox="0 0 800 1200" aria-hidden="true">
      <path d="M0 928 C150 890 300 878 450 902 C600 928 700 950 800 878 V1200 H0 Z" fill="var(--ink)"/>
      <path d="M0 958 C200 900 350 905 520 962 C650 1002 740 982 800 892 V1200 H0 Z" fill="var(--blue)"/>
    </svg>

    <h1>
      <span class="line slab headline headline--one">WORRIED ABOUT</span>
      <span class="line slab headline headline--two">THINNING HAIR?</span>
    </h1>
    <p class="line sans stat">2 out of 3 Men will have visible hair loss by <span class="stat__age">AGE 35.</span></p>

    <div class="news-shadow"></div>
    <div class="news-box"></div>
    <p class="line slab news-lead">THE GOOD NEWS IS THAT YOUR</p>
    <p class="line sans news-body news-body--one">Barber or stylist can tell you how to</p>
    <p class="line sans news-body news-body--two">Stop the loss &amp; grow back your hair.</p>

    <p class="line slab cta">JUST ASK.</p>
    <p class="line slab program">THE BRISK LATTICE PROGRAM FROM</p>
    <p class="line slab web">www.quellvantinfo.example</p>

    <p class="line slab company">THE MARLOW PINE COMPANY</p>
    <p class="line sans tagline">New Science. No Surgery. Your Hair.</p>
  </main>
</body>
</html>
```